Software Company Business Card

We are looking for a new design of our business card. The design will also be used in the rest of our branding and marketing materials as we want to keep it all uniform. We sell POS software to fine/luxury jewelers and also offer other business services as well to help the jeweler manage their business and need something more updated, technical and fresh, preferably more on the masculine side. We do not want any designs with gems in them but if possible would like to incorporate the circle and arrow in the logo into the design, but not a requirement if you can't make it work. I would like to see a variety of the mix. The colors need to remain our blue and orange and the logo can not change. The squiggly lines have been used as our corporate identity for over 20 years and its time to update. Our company name is TELK (Superior Counter Operations Platforms).

Target Market(s)

High End Jewelers

Industry/Entity Type

Software

Contact Information for Business Card

As seen in attached image

Requirements
Must have
• Our logo and the colors must remain the same. Blue is #d95d39 and Orange is #0f5682.
Nice to have
• The circle and arrow incorporated but not a requirement.
Should not have
• Anything jewelry or gem related.

```html
<!DOCTYPE html>
<html lang="en">
<head>
<meta charset="utf-8">
<title>TELK Business Card</title>
<link rel="stylesheet" href="https://fonts.googleapis.com/css2?family=Open+Sans:wght@400;600;700;800&display=swap">
<style>
  :root {
    --brand-blue: #0f5682;
    --brand-orange: #d95d39;
    --card-white: #ffffff;
    --backdrop: #cfcfcf;
    --text-light: #ffffff;
  }
  * { margin: 0; padding: 0; box-sizing: border-box; }
  html, body {
    width: 1200px; height: 873px; overflow: hidden;
    background: var(--backdrop);
    font-family: "Open Sans", Arial, sans-serif;
  }
  .stage {
    position: relative; width: 1200px; height: 873px;
    display: flex; align-items: center; justify-content: center; gap: 40px;
  }
  .card {
    position: relative; width: 540px; height: 309px;
    background: var(--card-white);
    box-shadow: 0 2px 6px rgba(0,0,0,0.18);
    overflow: hidden;
  }

  .panel-blue {
    position: absolute; left: 0; top: 0; width: 100%; height: 218px;
    background: var(--brand-blue);
  }
  .panel-orange {
    position: absolute; left: 0; bottom: 0; width: 100%; height: 72px;
    background: var(--brand-orange);
  }

  .holder { position: absolute; left: 38px; top: 30px; color: var(--text-light); }
  .holder-name { color: var(--brand-orange); font-weight: 700; font-size: 16px; line-height: 1.1; }
  .holder-title { font-size: 12px; line-height: 1.3; }

  .contact-list { position: absolute; left: 38px; top: 86px; list-style: none; color: var(--text-light); font-size: 12px; line-height: 16px; }
  .contact-list li { display: flex; align-items: center; gap: 5px; }
  .contact-icon { width: 8px; height: 8px; fill: var(--brand-orange); flex: none; }

  .postal { position: absolute; left: 230px; top: 86px; color: var(--text-light); font-size: 12px; line-height: 16px; font-style: normal; }

  .web { position: absolute; right: 36px; bottom: 28px; color: var(--text-light); font-size: 11px; }

  .brand-lockup {
    position: absolute; inset: 0;
    display: flex; align-items: center; justify-content: center;
  }
  .brand-name { color: var(--brand-blue); font-weight: 800; font-size: 64px; letter-spacing: 2px; line-height: 1; }
</style>
</head>
<body>
<main class="stage">
  <section class="card card-front" aria-label="Business card front">
    <div class="panel-blue" aria-hidden="true"></div>
    <div class="panel-orange" aria-hidden="true"></div>
    <div class="holder">
      <p class="holder-name">Dorian Whitcombe</p>
      <p class="holder-title">Founder</p>
    </div>
    <ul class="contact-list">
      <li><svg class="contact-icon" viewBox="0 0 10 10"><path d="M2 0 L4 2 L3 3.5 Q4.5 6 6.5 7 L8 6 L10 8 L8.5 10 Q3 9 0 1.5 Z"/></svg>1-800-555-0147 (Toll Free)</li>
      <li><svg class="contact-icon" viewBox="0 0 10 10"><path d="M2 0 L4 2 L3 3.5 Q4.5 6 6.5 7 L8 6 L10 8 L8.5 10 Q3 9 0 1.5 Z"/></svg>702-555-0182 (Phone)</li>
      <li><svg class="contact-icon" viewBox="0 0 10 10"><path d="M2 0 H8 V3 H2 Z M0 4 H10 V8 H0 Z M2 8 H8 V10 H2 Z"/></svg>702-555-0190</li>
      <li><svg class="contact-icon" viewBox="0 0 10 10"><path d="M0 2 H10 V8 H0 Z"/></svg>info@telkusa.com</li>
    </ul>
    <address class="postal">TELK USA<br>P.O. Box 410288<br>Silver Ridge<br>NV 89031 USA</address>
    <p class="web">www.telkusa.com</p>
  </section>

  <section class="card card-back" aria-label="Business card back">
    <div class="brand-lockup">
      <span class="brand-name">TELK</span>
    </div>
  </section>
</main>
</body>
</html>
```